VELMORHAVEN

We just changed our name from Quillhacks to Velmorrhaven so we need a new website. have been in the catering &special events business for 36 years . We are an in house caterer with homemade food and best around our name has always hurt us so we changed it and want a new web site to go with it. The current website Quillhacks banquet center .com can be viewed but, is horrible. I have been to many website companies in the past years and have never had a profesinal website. What brides want to see on the web are pictures and I feel they do not necessarily have to be from this facility they can be stock photos that resemble this place.

weddings partys

Business

5+ page

Must have
• pictures
Nice to have
• we have done functions for the king of Jordan on his plane and other famous people including celebrities and stars. This was when we were doing airline catering years ago, but, does not matter if plane or our facility they do not need to know that. Their were many people who have come to us from all over the world for private functions. Consider the possibilities memorable Weddings, exciting anniversaries and birthday parties .

```html
<!DOCTYPE html>
<html lang="en">
<head>
<meta charset="utf-8">
<title>Velmorrhaven – Banquet &amp; Conference Center</title>
<link href="https://fonts.googleapis.com/css2?family=Roboto:ital,wght@0,300;0,400;0,500;0,700;1,400&display=swap" rel="stylesheet">
<style>
:root{
  --red:#d8313a;
  --plum:#4a1f35;
  --ink:#333333;
  --muted:#7a7a7a;
  --band:#dcdbd6;
  --dark:#2a2a2a;
  --darker:#1e1e1e;
  --white:#ffffff;
  --line:#d9d9d9;
}
*{box-sizing:border-box;margin:0;padding:0}
html,body{width:1200px;height:5000px;overflow:hidden}
body{font-family:'Roboto',Arial,sans-serif;color:var(--ink);background:var(--white);position:relative}
.section{position:absolute;left:0;width:1200px}

/* header */
.site-header{top:0;height:60px;background:var(--white);box-shadow:0 1px 4px rgba(0,0,0,.08);z-index:2}
.brand{position:absolute;left:40px;top:16px;font-size:26px;font-weight:500;letter-spacing:.5px;color:var(--ink)}
.main-nav{position:absolute;left:395px;top:0;display:flex;height:60px;align-items:center;gap:30px}
.main-nav a{font-size:14px;font-weight:500;color:#555;text-decoration:none;text-transform:uppercase}
.header-phone{position:absolute;right:48px;top:20px;font-size:17px;font-weight:500;color:#444;display:flex;align-items:center;gap:8px}

/* hero */
.hero{top:60px;height:625px;background:
  linear-gradient(180deg,rgba(60,40,25,.55) 0%,rgba(0,0,0,0) 30%,rgba(0,0,0,0) 70%,rgba(60,40,25,.45) 100%),
  linear-gradient(90deg,#7d6a55 0%,#c9b79e 30%,#e4d8c6 50%,#c3b096 70%,#6f5c47 100%)}
.hero-badge{position:absolute;left:330px;top:360px;width:540px;height:120px;border-radius:60px;background:var(--plum);color:var(--white);display:flex;align-items:center;justify-content:center;font-size:52px;font-weight:300}
.hero-badge strong{font-weight:700;margin-left:12px}

/* welcome */
.welcome{top:700px;height:290px}
.section-title{position:absolute;left:0;width:100%;text-align:center;font-size:30px;font-weight:400;color:var(--ink)}
.section-title span{color:var(--red);font-weight:700}
.title-rule{position:absolute;height:1px;background:var(--line)}
.welcome-text{position:absolute;left:73px;width:1054px;top:100px;text-align:center;font-size:15px;line-height:1.65;color:var(--muted)}
.welcome-text p+p{margin-top:22px}

/* slanted bands */
.band{background:var(--band)}
.services{top:1000px;height:775px;clip-path:polygon(0 6%,100% 0,100% 94%,0 100%)}
.section-tab{position:absolute;left:73px;height:74px;background:var(--red);color:var(--white);font-size:30px;font-weight:400;padding:20px 0 0 30px;width:300px;clip-path:polygon(0 0,100% 0,88% 100%,0 100%)}
.section-tab strong{font-weight:700}
.service-grid{position:absolute;left:73px;top:150px;width:1054px;display:grid;grid-template-columns:repeat(4,243px);column-gap:27px;row-gap:35px}
.service-photo{height:175px}
.service-name{font-size:19px;font-weight:500;margin-top:14px;color:#333}

/* featured */
.featured{top:1800px;height:360px}
.featured-col{position:absolute;top:0;width:325px}
.featured-col h3{font-size:21px;font-weight:400;color:#333;margin-bottom:22px}
.featured-col h3 span{color:var(--red);font-weight:700}
.featured-col p{font-size:14px;line-height:1.7;color:var(--muted)}
.read-more{display:block;margin-top:26px;font-size:14px;font-weight:700;color:#333}

/* events */
.events{top:2170px;height:650px;clip-path:polygon(0 0,100% 8%,100% 100%,0 92%)}
.event-grid{position:absolute;left:73px;top:180px;width:1054px;display:grid;grid-template-columns:repeat(4,247px);column-gap:22px}
.event-card{background:var(--white);height:400px;position:relative}
.event-photo{height:185px}
.event-date{position:absolute;left:0;top:145px;background:var(--white);padding:6px 12px;font-size:28px;font-weight:700;color:#333}
.event-date small{font-size:11px;font-weight:500;margin-left:4px;vertical-align:middle}
.event-body{padding:18px 22px}
.event-body h4{font-size:15px;font-weight:700;line-height:1.4;color:#333}
.event-body p{font-size:13px;line-height:1.6;color:var(--muted);margin-top:14px}
.event-body .read-more{margin-top:12px;font-size:13px}

/* gallery */
.gallery{top:2920px;height:740px}
.gallery-grid{position:absolute;left:73px;top:97px;width:1054px;height:543px;display:grid;grid-template-columns:repeat(4,1fr);column-gap:14px}
.gallery-col{display:flex;flex-direction:column;gap:10px}
.gallery-col div{flex:1}
.gallery-button{position:absolute;left:470px;top:690px;width:260px;height:46px;border:1px solid #bbb;display:flex;align-items:center;justify-content:center;font-size:14px;font-weight:500;color:#333}

/* testimonial */
.testimonial{top:3740px;height:367px;background:linear-gradient(90deg,#1c1c1c,#2e2b28 60%,#24201d)}
.testimonial h2{position:absolute;left:73px;top:30px;font-size:26px;font-weight:300;color:var(--white)}
.testimonial h2 strong{font-weight:500}
.avatar{position:absolute;left:80px;top:105px;width:110px;height:110px;border-radius:50%;background:#8a7766;border:4px solid var(--white)}
.reviewer{position:absolute;left:70px;top:228px;width:130px;text-align:center;color:var(--white);font-size:13px;line-height:1.4}
.quote{position:absolute;left:225px;top:110px;width:500px;font-style:italic;font-size:17px;line-height:1.7;color:var(--white)}
.dots{position:absolute;left:225px;top:315px;display:flex;gap:8px}
.dots i{width:10px;height:10px;border-radius:50%;background:#777;display:block}
.dots i:first-child{background:var(--white)}

.help-box{position:absolute;left:783px;top:3710px;width:344px;height:435px;background:var(--red);z-index:2}
.help-box h2{height:66px;padding:18px 0 0 55px;font-size:26px;font-weight:300;color:var(--white)}
.help-box h2 strong{font-weight:700}
.help-form{position:absolute;left:28px;top:66px;width:300px;height:340px;background:#252525;padding:12px 12px}
.field{height:36px;border:1px solid #555;background:var(--white);margin-bottom:12px;font-size:12px;color:#777;padding:10px 10px}
.field.message{height:90px}
.submit{height:42px;background:#151515;color:var(--white);font-weight:700;font-size:14px;display:flex;align-items:center;justify-content:center}

/* contact */
.contact{top:4145px;height:455px;background:linear-gradient(180deg,#ffffff 0%,#ececec 50%,#ffffff 100%)}
.eyebrow{position:absolute;left:0;width:100%;top:85px;text-align:center;font-size:15px;font-weight:500;letter-spacing:1px;color:#555}
.contact h2{position:absolute;left:0;width:100%;top:140px;text-align:center;font-size:44px;font-weight:300;color:#444}
.contact h2 span{color:var(--red);font-weight:500}
.contact-lead{position:absolute;left:0;width:100%;top:212px;text-align:center;font-size:15px;color:var(--muted)}
.phone-icon{position:absolute;left:584px;top:250px;width:32px;height:32px;border-radius:50%;background:var(--red);display:flex;align-items:center;justify-content:center}
.contact-numbers{position:absolute;left:400px;width:400px;top:290px;display:flex;justify-content:space-around;text-align:center}
.contact-numbers span{display:block;font-size:15px;color:var(--muted)}
.contact-numbers strong{font-size:22px;font-weight:500;color:#333}
.email-button{position:absolute;left:465px;top:372px;width:270px;height:40px;border:1px solid var(--red);color:var(--red);font-size:14px;display:flex;align-items:center;justify-content:center;background:var(--white)}

/* map */
.map{top:4600px;height:120px;background:linear-gradient(160deg,#e6e4dc,#d9dfd0 50%,#e8e6df)}
.address-bar{position:absolute;left:320px;top:0;height:34px;display:flex;align-items:stretch;font-size:13px}
.address-bar b{background:var(--red);color:var(--white);padding:9px 14px;font-weight:700}
.address-bar span{background:#3a3a3a;color:var(--white);padding:9px 16px}
.map-pin{position:absolute;left:622px;top:62px}

/* footer */
.site-footer{top:4720px;height:280px;background:var(--darker)}
.footer-nav{position:absolute;left:0;width:100%;top:138px;display:flex;justify-content:center;gap:32px}
.footer-nav a{color:var(--white);font-size:14px;font-weight:500;text-decoration:none;text-transform:uppercase}
.social{position:absolute;left:0;width:100%;top:180px;display:flex;justify-content:center;gap:16px}
.social i{display:block;width:22px;height:22px;border-radius:50%;background:#cfcfcf}
.copyright{position:absolute;left:0;width:100%;top:230px;text-align:center;font-size:12px;color:#888}
</style>
</head>
<body>

<header class="section site-header">
  <div class="brand">VELMORRHAVEN</div>
  <nav class="main-nav">
    <a href="#">Home</a><a href="#">About Us</a><a href="#">Services</a><a href="#">Gallery</a><a href="#">Contact Us</a>
  </nav>
  <div class="header-phone">
    <svg width="18" height="18" viewBox="0 0 24 24"><path fill="#444" d="M6.6 10.8a15 15 0 0 0 6.6 6.6l2.2-2.2c.3-.3.7-.4 1-.2 1.1.4 2.3.6 3.6.6.6 0 1 .4 1 1V20c0 .6-.4 1-1 1A17 17 0 0 1 3 4c0-.6.4-1 1-1h3.5c.6 0 1 .4 1 1 0 1.3.2 2.5.6 3.6.1.3 0 .7-.2 1z"/></svg>
    (555) 014-2379
  </div>
</header>

<section class="section hero" role="img" aria-label="Photo of a rustic barn ballroom set for a wedding reception with chandeliers and white chairs">
  <div class="hero-badge">Beautiful <strong>Venues.</strong></div>
</section>

<section class="section welcome">
  <div class="title-rule" style="left:73px;width:300px;top:24px"></div>
  <div class="title-rule" style="left:827px;width:300px;top:24px"></div>
  <h1 class="section-title" style="top:6px">Welcome to <span>Velmorrhaven</span></h1>
  <div class="welcome-text">
    <p>Imagine your wedding in a picturesque Alder Valley rural setting with an elegant grand ballroom to delight your guests along with a fabulous glass enclosed atrium. Velmorrhaven's beautiful setting includes a huge outdoor reception area and terrace with a magnificent garden.</p>
    <p>Velmorrhaven features mouth watering homemade entrees and offers award winning fruit and cheese displays. All this includes the most special attention to answer your every want and desire for a fantastic wedding reception. Velmorrhaven also features custom catering for all types of social and professional events. And all at a surprisingly reasonable price to you...</p>
  </div>
</section>

<section class="section band services">
  <div class="section-tab" style="top:62px">Our <strong>Services</strong></div>
  <div class="service-grid">
    <div><div class="service-photo" role="img" aria-label="Photo of a bride and groom at a wedding table" style="background:linear-gradient(135deg,#e3d9ce,#a89684)"></div><div class="service-name">Weddings</div></div>
    <div><div class="service-photo" role="img" aria-label="Photo of a banquet hall set with round tables" style="background:linear-gradient(135deg,#6e4a2a,#c09060)"></div><div class="service-name">Banquets</div></div>
    <div><div class="service-photo" role="img" aria-label="Photo of guests at a fundraising event" style="background:linear-gradient(135deg,#8a6a58,#d0ae92)"></div><div class="service-name">Fund Raisers</div></div>
    <div><div class="service-photo" role="img" aria-label="Photo of a retirement party gathering" style="background:linear-gradient(135deg,#c4b9ae,#7f7368)"></div><div class="service-name">Retirement Parties</div></div>
    <div><div class="service-photo" role="img" aria-label="Photo of friends celebrating a birthday under party lights" style="background:linear-gradient(135deg,#3a1a6a,#c0308a)"></div><div class="service-name">Birthdays</div></div>
    <div><div class="service-photo" role="img" aria-label="Photo of a dimly lit bar counter" style="background:linear-gradient(135deg,#1c140e,#5a3c22)"></div><div class="service-name">Bar</div></div>
    <div><div class="service-photo" role="img" aria-label="Photo of a dance floor lit for a bat mitzvah" style="background:linear-gradient(135deg,#1a1030,#5a3a8a)"></div><div class="service-name">Bat Mitzvahs</div></div>
    <div><div class="service-photo" role="img" aria-label="Photo of an elegant event room with warm lights" style="background:linear-gradient(135deg,#2a1a18,#7a4a3a)"></div><div class="service-name">All Occasions</div></div>
  </div>
</section>

<section class="section featured">
  <div class="featured-col" style="left:73px">
    <h3>Featured <span>Professional</span></h3>
    <p>Lorem ipsum dolor sit amet, consectetur adipiscing elit, sed do eiusmod tempor incididunt ut labore et dolore magna aliqua. Ut enim ad minim veniam, quis nostrud exercitation ullamco laboris nisi ut aliquip ex ea commodo consequat. Duis aute irure dolor in reprehenderit in voluptate velit esse cillum dolore eu fugiat nulla pariatur. Excepteur sint occaecat cupidatat non proident, sunt in culpa qui officia deserunt mollit anim id est laborum.</p>
    <span class="read-more">Read More →</span>
  </div>
  <div class="featured-col" style="left:433px">
    <h3>We <span>Are Number One</span></h3>
    <p>Lorem ipsum dolor sit amet, consectetur adipiscing elit, sed do eiusmod tempor incididunt ut labore et dolore magna aliqua. Ut enim ad minim veniam, quis nostrud exercitation ullamco laboris nisi ut aliquip ex ea commodo consequat. Duis aute irure dolor in reprehenderit in voluptate velit esse cillum dolore eu fugiat nulla pariatur. Excepteur sint occaecat cupidatat non proident, sunt in culpa qui officia deserunt mollit anim id est laborum.</p>
    <span class="read-more">Read More →</span>
  </div>
  <div class="featured-col" style="left:793px">
    <h3>Featured <span>Venue</span></h3>
    <p>Lorem ipsum dolor sit amet, consectetur adipiscing elit, sed do eiusmod tempor incididunt ut labore et dolore magna aliqua. Ut enim ad minim veniam, quis nostrud exercitation ullamco laboris nisi ut aliquip ex ea commodo consequat. Duis aute irure dolor in reprehenderit in voluptate velit esse cillum dolore eu fugiat nulla pariatur. Excepteur sint occaecat cupidatat non proident, sunt in culpa qui officia deserunt mollit anim id est laborum.</p>
    <span class="read-more">Read More →</span>
  </div>
</section>

<section class="section band events">
  <div class="section-tab" style="top:75px">Feature <strong>Event</strong></div>
  <div class="event-grid">
    <article class="event-card">
      <div class="event-photo" role="img" aria-label="Photo of a ballroom with chandeliers" style="background:linear-gradient(135deg,#5a4a30,#c8b68a)"></div>
      <div class="event-date">19 <small>OCT</small></div>
      <div class="event-body"><h4>Lorem ipsum dolor sit amet, consectetur adipiscing elit.</h4><p>Sed ut perspiciatis unde omnis iste natus error sit voluptatem accusantium doloremque laudantium, totam.</p><span class="read-more">Read More →</span></div>
    </article>
    <article class="event-card">
      <div class="event-photo" role="img" aria-label="Photo of a guest in an evening dress" style="background:linear-gradient(135deg,#2a2420,#a08a78)"></div>
      <div class="event-date">19 <small>OCT</small></div>
      <div class="event-body"><h4>Lorem ipsum dolor sit amet, consectetur adipiscing elit.</h4><p>Sed ut perspiciatis unde omnis iste natus error sit voluptatem accusantium doloremque laudantium, totam.</p><span class="read-more">Read More →</span></div>
    </article>
    <article class="event-card">
      <div class="event-photo" role="img" aria-label="Photo of a catered buffet platter" style="background:linear-gradient(135deg,#6a4a20,#d0a050)"></div>
      <div class="event-date">19 <small>OCT</small></div>
      <div class="event-body"><h4>Lorem ipsum dolor sit amet, consectetur adipiscing elit.</h4><p>Sed ut perspiciatis unde omnis iste natus error sit voluptatem accusantium doloremque laudantium, totam.</p><span class="read-more">Read More →</span></div>
    </article>
    <article class="event-card">
      <div class="event-photo" role="img" aria-label="Photo of a reception room with set tables" style="background:linear-gradient(135deg,#7a6248,#d6c2a0)"></div>
      <div class="event-date">19 <small>OCT</small></div>
      <div class="event-body"><h4>Lorem ipsum dolor sit amet, consectetur adipiscing elit.</h4><p>Sed ut perspiciatis unde omnis iste natus error sit voluptatem accusantium doloremque laudantium, totam.</p><span class="read-more">Read More →</span></div>
    </article>
  </div>
</section>

<section class="section gallery">
  <div class="title-rule" style="left:73px;width:390px;top:37px"></div>
  <div class="title-rule" style="left:737px;width:390px;top:37px"></div>
  <h2 class="section-title" style="top:18px">Photo <span>Gallery</span></h2>
  <div class="gallery-grid">
    <div class="gallery-col">
      <div role="img" aria-label="Photo of a decorated fireplace with flowers" style="flex:1.6;background:linear-gradient(135deg,#2a2a2a,#8a8478)"></div>
      <div role="img" aria-label="Photo of a hall with round tables" style="background:linear-gradient(135deg,#3a3a3a,#7a7a7a)"></div>
    </div>
    <div class="gallery-col">
      <div role="img" aria-label="Photo of a plated dinner" style="background:linear-gradient(135deg,#3a2a20,#a07a5a)"></div>
      <div role="img" aria-label="Photo of a lit garden terrace at dusk" style="flex:1.2;background:linear-gradient(180deg,#5a6a8a,#2a3a2a)"></div>
      <div role="img" aria-label="Photo of a dark reception room" style="background:linear-gradient(135deg,#1a1a1a,#4a4a4a)"></div>
    </div>
    <div class="gallery-col">
      <div role="img" aria-label="Photo of a snowy night outside the venue" style="background:linear-gradient(135deg,#1a2a5a,#6a8ac0)"></div>
      <div role="img" aria-label="Photo of a corridor with warm lights" style="flex:1.2;background:linear-gradient(135deg,#2a1a10,#8a5a2a)"></div>
      <div role="img" aria-label="Photo of a dance floor with purple lights" style="background:linear-gradient(135deg,#3a1a8a,#c040c0)"></div>
    </div>
    <div class="gallery-col">
      <div role="img" aria-label="Photo of a catered food table" style="background:linear-gradient(135deg,#5a1a10,#c0603a)"></div>
      <div role="img" aria-label="Photo of a bride standing in a doorway" style="flex:2.2;background:linear-gradient(135deg,#1a2a20,#c8c4bc)"></div>
    </div>
  </div>
  <div class="gallery-button">View All Photos in The Gallery →</div>
</section>

<section class="section testimonial">
  <h2>What <strong>People Are Saying</strong></h2>
  <div class="avatar" role="img" aria-label="Portrait of a reviewer"></div>
  <div class="reviewer">Maren<br>Ellsworth</div>
  <blockquote class="quote">"Lorem ipsum dolor sit amet, consectetur adipiscing elit, sed do eiusmod tempor incididunt ut labore et dolore magna aliqua. Ut enim ad minim veniam, quis nostrud exercitation ullamco laboris nisi ut aliquip ex ea commodo consequat. Duis aute irure dolor in reprehenderit in voluptate velit esse cillum dolore eu fugiat nulla pariatur."</blockquote>
  <div class="dots"><i></i><i></i><i></i><i></i><i></i><i></i></div>
</section>

<aside class="help-box">
  <h2>How <strong>Can We Help?</strong></h2>
  <div class="help-form">
    <div class="field">First Name</div>
    <div class="field">Last Name</div>
    <div class="field">E-Mail Address</div>
    <div class="field">Phone Number</div>
    <div class="field message">Your Message</div>
    <div class="submit">SUBMIT</div>
  </div>
</aside>

<section class="section contact">
  <div class="eyebrow">CONTACT US</div>
  <h2>Let's <span>Get In Touch</span></h2>
  <p class="contact-lead">Tell us some more about what you're looking for and how we can help</p>
  <div class="phone-icon"><svg width="16" height="16" viewBox="0 0 24 24"><path fill="#fff" d="M6.6 10.8a15 15 0 0 0 6.6 6.6l2.2-2.2c.3-.3.7-.4 1-.2 1.1.4 2.3.6 3.6.6.6 0 1 .4 1 1V20c0 .6-.4 1-1 1A17 17 0 0 1 3 4c0-.6.4-1 1-1h3.5c.6 0 1 .4 1 1 0 1.3.2 2.5.6 3.6.1.3 0 .7-.2 1z"/></svg></div>
  <div class="contact-numbers">
    <div><span>Phone</span><strong>(555) 014-2379</strong></div>
    <div><span>Fax</span><strong>(555) 014-2160</strong></div>
  </div>
  <div class="email-button">events@velmorrhaven.example</div>
</section>

<section class="section map" role="img" aria-label="Street map showing the venue location">
  <div class="address-bar"><b>ADDRESS</b><span>Velmorrhaven Banquet &amp; Conf Center, 120 Alder Ridge Rd, Brookfield Vale 04417</span></div>
  <svg class="map-pin" width="22" height="32" viewBox="0 0 22 32"><path fill="#d8313a" d="M11 0C5 0 0 5 0 11c0 8 11 21 11 21s11-13 11-21C22 5 17 0 11 0z"/><circle cx="11" cy="11" r="4" fill="#fff"/></svg>
</section>

<footer class="section site-footer">
  <nav class="footer-nav">
    <a href="#">Home</a><a href="#">About Us</a><a href="#">Services</a><a href="#">Gallery</a><a href="#">Contact Us</a>
  </nav>
  <div class="social"><i></i><i></i><i></i><i></i><i></i></div>
  <div class="copyright">Copyright © 2017 Velmorrhaven</div>
</footer>

</body>
</html>
```